Business Card Design for Law firm - already have logo

Now that we have a logo, we need a business card design - our logo is attached -it is salaryman font if that helps - we would like a file that can be uploaded to cardquill (www.cardquill-example.com) using the logo and with the following information on it:
Quenby Law Firm, P.C.
Delwyn Quenby, Esq.
5817 SW 19th Ave.
Portland, OR 97213
971.555.0142 phone
971.555.0187 fax
del@quenby-example.net
Voicenook: delquenby
Talkline: delwyn.quenby@mailbox-example.com
Target Market(s)
our business cards are distributed to corporate executives, technology professionals and healthcare providers
Industry/Entity Type
Business
Look and feel

```html
<!DOCTYPE html>
<html lang="en">
<head>
<meta charset="utf-8">
<title>Quenby Law Firm, P.C. – Business Card</title>
<link href="https://fonts.googleapis.com/css2?family=Hind:wght@400;600&display=swap" rel="stylesheet">
<style>
  :root {
    --backdrop: #e4e8ee;
    --card: #fbfbfb;
    --ink: #2a2a2a;
    --ink-soft: #3a3a3a;
    --block: #262626;
  }
  * { box-sizing: border-box; margin: 0; padding: 0; }
  html, body {
    width: 1200px;
    height: 1000px;
    overflow: hidden;
    background: var(--backdrop);
    font-family: "Hind", Arial, sans-serif;
    color: var(--ink);
  }
  .stage {
    width: 1200px;
    height: 1000px;
    display: flex;
    align-items: center;
    justify-content: center;
  }
  .card {
    position: relative;
    width: 440px;
    height: 770px;
    background: var(--card);
    box-shadow: 0 6px 24px rgba(0,0,0,0.12);
    text-align: center;
  }
  .brand {
    position: absolute;
    top: 0;
    left: 22px;
    right: 22px;
    height: 150px;
    display: flex;
    align-items: center;
    justify-content: center;
    gap: 14px;
  }
  .brand-mark {
    width: 22px;
    height: 22px;
    background: var(--block);
  }
  .brand-name {
    font-weight: 600;
    font-size: 52px;
    letter-spacing: 0.16em;
    color: var(--ink);
    line-height: 1;
  }
  .details {
    position: absolute;
    top: 188px;
    left: 0;
    right: 0;
    display: flex;
    flex-direction: column;
    align-items: center;
  }
  .details p, .details h1 { line-height: 32px; height: 32px; white-space: nowrap; }
  .firm {
    font-weight: 600;
    font-size: 25px;
    letter-spacing: 0.06em;
    text-transform: uppercase;
    margin-bottom: 38px;
  }
  .line-strong {
    font-weight: 600;
    font-size: 21px;
    margin-bottom: 26px;
  }
  .line-strong sup { font-size: 12px; line-height: 0; }
  .contact {
    font-weight: 400;
    font-size: 21px;
    margin-bottom: 26px;
    color: var(--ink-soft);
  }
  .contact b { font-weight: 600; color: var(--ink); margin-right: 4px; }
  .handle {
    font-weight: 400;
    font-size: 18px;
    margin-bottom: 22px;
    color: var(--ink-soft);
  }
  .foot-band {
    position: absolute;
    bottom: 0;
    left: 14px;
    right: 14px;
    display: flex;
    justify-content: space-between;
  }
  .foot-band span {
    width: 52px;
    height: 28px;
    background: var(--block);
  }
</style>
</head>
<body>
  <main class="stage">
    <article class="card">
      <header class="brand">
        <span class="brand-name">QUENBY</span>
        <span class="brand-mark"></span>
      </header>
      <section class="details">
        <h1 class="firm">Quenby Law Firm, P.C.</h1>
        <p class="line-strong">Delwyn Quenby, Esq.</p>
        <p class="line-strong">5817 SW 19<sup>th</sup> Ave.</p>
        <p class="line-strong">Alderbrook, OR 97000.</p>
        <p class="contact"><b>P</b>971.555.0142</p>
        <p class="contact"><b>F</b>971.555.0187</p>
        <p class="contact"><b>E</b>del@quenby-example.net</p>
        <p class="handle">Voicenook: delquenby</p>
        <p class="handle">Talkline: delwyn.quenby@mailbox-example.com</p>
      </section>
      <footer class="foot-band" aria-hidden="true">
        <span></span><span></span><span></span><span></span><span></span><span></span><span></span>
      </footer>
    </article>
  </main>
</body>
</html>
```